Business Card Design Project

We need a buisness card for a new digital sinage company. Our target cliants are small to mediaum buisness who want to advertise on out digital sinage network

Target Market(s)

Small to medium buisness

Industry/Entity Type

Digital

Requirements
Must have
• Must have logo

```html
<!DOCTYPE html>
<html lang="en">
<head>
<meta charset="utf-8">
<title>Vyno – Business Card Set</title>
<link rel="stylesheet" href="https://fonts.googleapis.com/css2?family=Archivo+Black&family=Arimo:wght@400&family=PT+Sans&display=swap">
<style>
  :root {
    --stage-bg: #ece8e3;
    --card-white: #ffffff;
    --card-black: #0b0b0b;
    --ink: #0d0d0d;
    --ink-soft: #222222;
    --brand-blue: #1c5fae;
    --band-blue-start: #2a9ad8;
    --band-blue-end: #1b4f9e;
    --band-green-start: #3e9e3a;
    --band-green-end: #8cc63f;
    --mark-blue: #2a8fd6;
    --label: #222222;
    --divider: #555555;
  }
  * { box-sizing: border-box; margin: 0; padding: 0; }
  html, body { width: 1200px; height: 788px; overflow: hidden; background: var(--stage-bg); }
  .stage { position: relative; width: 1200px; height: 788px; }

  .side-label {
    position: absolute; width: 525px; text-align: center;
    font-family: "PT Sans", sans-serif; font-size: 22px; color: var(--label);
  }

  .card {
    position: absolute; width: 525px; height: 300px; border-radius: 18px;
    background: var(--card-white); overflow: hidden;
    box-shadow: 0 2px 6px rgba(0,0,0,0.12);
  }
  .card--dark { background: var(--card-black); }
  .card--front { left: 54px; top: 74px; }
  .card--back-1 { left: 622px; top: 74px; }
  .card--back-2 { left: 54px; top: 445px; }
  .card--back-3 { left: 622px; top: 445px; }

  .wordmark {
    position: absolute; font-family: "Archivo Black", sans-serif;
    color: var(--ink); line-height: 1; letter-spacing: -1px;
  }
  .card--dark .wordmark { color: var(--card-white); }
  .brand-square { position: absolute; background: var(--mark-blue); border-radius: 4px; }

  .web-line {
    position: absolute; left: 0; width: 100%; text-align: center;
    font-family: "Arimo", sans-serif; font-size: 15px; letter-spacing: 5.5px;
    color: var(--ink-soft);
  }
  .card--dark .web-line { color: var(--card-white); }

  .contact {
    position: absolute; left: 309px; top: 118px; padding-left: 12px;
    border-left: 1px solid var(--divider); height: 92px;
    font-family: "Arimo", sans-serif; color: var(--ink-soft); font-size: 13.5px; line-height: 1.3;
  }
  .contact__name { color: var(--brand-blue); font-size: 17px; margin-top: 2px; margin-bottom: 8px; }
  .contact__phone { margin-bottom: 8px; }

  .front-bands { position: absolute; left: 0; bottom: 0; }
  .online {
    position: absolute; left: 321px; top: 252px;
    font-family: "Arimo", sans-serif; font-size: 13px; line-height: 1.35; color: var(--card-white);
  }
</style>
</head>
<body>
<main class="stage">
  <div class="side-label" style="left:54px; top:32px;">Front</div>
  <div class="side-label" style="left:622px; top:32px;">Back - 1</div>
  <div class="side-label" style="left:54px; top:403px;">Back - 2</div>
  <div class="side-label" style="left:622px; top:403px;">Back - 3</div>

  <section class="card card--front" aria-label="Card front">
    <div class="brand-square" style="left:22px; top:88px; width:64px; height:64px;"></div>
    <div class="wordmark" style="left:138px; top:112px; font-size:62px;">Vyno</div>
    <div class="contact">
      <div class="contact__name">Marcus Telford</div>
      <div class="contact__phone">phone : 0400123987</div>
      <div>PO Box 514</div>
      <div>Karratha Bay, WA 6799</div>
    </div>
    <svg class="front-bands" width="525" height="60" viewBox="0 0 525 60" aria-hidden="true">
      <defs>
        <linearGradient id="bandBlue" x1="0" x2="1">
          <stop offset="0" stop-color="var(--band-blue-end)"/>
          <stop offset="1" stop-color="var(--band-blue-start)"/>
        </linearGradient>
        <linearGradient id="bandGreen" x1="0" x2="1">
          <stop offset="0" stop-color="var(--band-green-start)"/>
          <stop offset="1" stop-color="var(--band-green-end)"/>
        </linearGradient>
      </defs>
      <polygon points="0,34 262,34 248,48 0,48" fill="url(#bandBlue)"/>
      <polygon points="291,8 525,8 525,60 0,60 0,52 250,52" fill="url(#bandGreen)"/>
    </svg>
    <div class="online">
      <div>email : marcus@vyno.com.au</div>
      <div>web : www.vyno.com.au</div>
    </div>
  </section>

  <section class="card card--back-1" aria-label="Card back, option 1">
    <div class="brand-square" style="left:110px; top:112px; width:100px; height:100px;"></div>
    <div class="wordmark" style="left:244px; top:136px; font-size:80px;">Vyno</div>
    <div class="web-line" style="top:260px;">www.vyno.com.au</div>
  </section>

  <section class="card card--back-2" aria-label="Card back, option 2">
    <div class="wordmark" style="left:0; width:100%; text-align:center; top:84px; font-size:150px;">Vyno</div>
    <div class="web-line" style="top:258px;">www.vyno.com.au</div>
  </section>

  <section class="card card--back-3 card--dark" aria-label="Card back, option 3">
    <div class="brand-square" style="left:110px; top:110px; width:100px; height:100px;"></div>
    <div class="wordmark" style="left:244px; top:134px; font-size:80px;">Vyno</div>
    <div class="web-line" style="top:258px;">www.vyno.com.au</div>
  </section>
</main>
</body>
</html>
```